Verdalunex webpage design

We are offering eco/sustainable theme vacations and make them bookable via our site. Our reference site is www.voyelmora.com. We want something similar but with a bit more creativity and elegant design. In our colors, which would depend on our logo colors.

NB: WE ARE NOT ASKING FOR A FULL BLOWN SITE. WE NEED 2 PAGE DESIGN FOR THE FIRST IMPRESSION. AFTER THAT WE CREATE A BUDGET FOR COMPLETION OF THE PROJECT.

Target Market(s)

Eco/Sustainable tourism.

Industry/Entity Type

Tourism

Coding

Coded - Design and coding required

Number of Pages Required

2 page

Requirements
Must have
• Reference site is voyelmora.com. But be creative and design something a bit different and more beautiful.
• NB: WE ARE NOT ASKING FOR A FULL BLOWN SITE. WE NEED 2 PAGE DESIGN FOR THE FIRST IMPRESSION. AFTER THAT WE CREATE A BUDGET FOR COMPLETION OF THE PROJECT.
• Please see our logo.

```html
<!DOCTYPE html>
<html lang="en">
<head>
<meta charset="utf-8">
<title>Verdalunex – Travel Experiences</title>
<link href="https://fonts.googleapis.com/css2?family=Lato:wght@700;900&family=Roboto:wght@400;500;700&display=swap" rel="stylesheet">
<style>
:root{
  --navy:#0b1f8c;
  --blue:#1b82dc;
  --ink:#1d1d1d;
  --text:#555;
  --muted:#777;
  --line:#e3e3e3;
  --page:#f6f4f4;
  --white:#fff;
  --footer:#0c1c80;
}
*{box-sizing:border-box;margin:0;padding:0}
html,body{width:1200px;height:3332px;overflow:hidden}
body{position:relative;background:var(--page);font-family:Roboto,sans-serif;color:var(--text)}
.top-rule{position:absolute;left:0;top:0;width:1200px;height:3px;background:var(--blue)}

/* header */
.site-header{position:absolute;left:0;top:3px;width:1200px;height:127px;background:var(--white)}
.brand{position:absolute;left:111px;top:50px;font-family:Lato,sans-serif;font-weight:900;font-size:33px;color:var(--navy);letter-spacing:.2px}
.main-nav{position:absolute;left:488px;top:59px;display:flex;gap:30px}
.main-nav a{font-family:Roboto,sans-serif;font-weight:500;font-size:16px;color:var(--ink);text-decoration:none}
.btn-signup{position:absolute;left:963px;top:47px;width:125px;height:43px;background:var(--blue);color:var(--white);font-weight:500;font-size:16px;display:flex;align-items:center;justify-content:center;gap:6px}

/* hero */
.hero{position:absolute;left:0;top:130px;width:1200px;height:568px;background:linear-gradient(180deg,#27385a 0%,#4a4c63 30%,#8a5a38 55%,#c1752c 68%,#3b3f55 82%,#1d2a44 100%)}
.hero-title{position:absolute;left:0;top:190px;width:1200px;text-align:center;font-family:Lato,sans-serif;font-weight:900;font-size:58px;color:var(--white);text-shadow:0 2px 6px rgba(0,0,0,.5)}
.hero-sub{position:absolute;left:230px;top:282px;width:740px;text-align:center;font-family:Roboto,sans-serif;font-weight:500;font-size:24px;line-height:37px;color:var(--white);text-shadow:0 2px 5px rgba(0,0,0,.6)}
.hero-arrow{position:absolute;top:236px;width:56px;height:56px;border-radius:50%;background:rgba(0,0,0,.55);display:flex;align-items:center;justify-content:center}
.hero-arrow.prev{left:53px}.hero-arrow.next{left:1091px}
.swoosh{position:absolute;top:690px}
.swoosh.left{left:0}.swoosh.right{left:1089px}

/* booking */
.booking{position:absolute;left:111px;top:613px;width:977px;height:254px;background:var(--white);box-shadow:0 2px 6px rgba(0,0,0,.08)}
.booking h2{position:absolute;left:0;top:48px;width:100%;text-align:center;font-family:Lato,sans-serif;font-weight:900;font-size:38px;color:var(--blue)}
.field{position:absolute;top:125px;width:275px}
.field label{display:block;font-weight:700;font-size:15px;color:var(--ink);margin-bottom:13px}
.field .input{height:43px;border:1px solid var(--line);display:flex;align-items:center;justify-content:space-between;padding:0 4px 0 16px;font-size:13px;color:#999}
.field .icon{width:35px;height:33px;background:var(--blue);display:flex;align-items:center;justify-content:center}

/* sidebar */
.widget{position:absolute;left:111px;width:256px}
.widget-tab{height:36px;width:182px;background:var(--blue);color:var(--white);font-weight:500;font-size:16px;line-height:36px;padding-left:16px;clip-path:polygon(0 0,150px 0,182px 100%,0 100%)}
.widget-body{background:var(--white);box-shadow:0 2px 5px rgba(0,0,0,.08);padding:22px 0 20px 24px}
.link-list{list-style:none}
.link-list li{font-size:15px;color:#444;height:32px;display:flex;align-items:center}
.link-list li::before{content:"»";margin-right:10px;color:#555;font-size:15px}
.opt-list{list-style:none}
.opt-list li{font-size:15px;color:#444;height:32px;display:flex;align-items:center;gap:10px}
.radio{width:13px;height:13px;border-radius:50%;border:2px solid #666}
.radio.on{border-color:var(--blue);background:radial-gradient(circle,var(--blue) 0 3px,#fff 3.5px)}
.check{width:12px;height:12px;border:1.5px solid #777;border-radius:2px}
.check.on{background:var(--blue);border-color:var(--blue)}
.btn-date{margin:16px 0 0 -7px;width:196px;height:40px;background:var(--navy);color:var(--white);font-weight:700;font-size:13px;display:flex;align-items:center;justify-content:center;gap:5px}

/* main column */
.about{position:absolute;left:414px;top:925px;width:674px;height:360px;background:var(--white);box-shadow:0 2px 6px rgba(0,0,0,.08);padding:38px 46px}
.about h3{font-family:Lato,sans-serif;font-weight:900;font-size:33px;color:var(--navy);margin-bottom:22px}
.about p{font-size:16px;line-height:30px;color:#555}
.btn-book{position:absolute;right:46px;bottom:44px;width:156px;height:44px;background:var(--blue);color:var(--white);font-weight:700;font-size:16px;display:flex;align-items:center;justify-content:center;gap:5px}

.trip{position:absolute;left:414px;width:674px;height:219px;background:var(--white);box-shadow:0 2px 6px rgba(0,0,0,.08)}
.trip-photo{position:absolute;left:13px;top:13px;width:197px;height:193px}
.trip h4{position:absolute;left:240px;top:22px;width:408px;font-weight:500;font-size:20px;line-height:29px;color:var(--ink);text-align:justify;text-align-last:justify}
.trip-features{position:absolute;left:240px;top:108px;list-style:none}
.trip-features li{font-size:14px;color:#555;height:35px;display:flex;align-items:center;gap:7px}
.trip-price{position:absolute;left:468px;top:92px;width:180px;height:102px;border-left:1px solid var(--line);text-align:right}
.trip-price .from{display:block;width:130px;margin-left:auto;text-align:center;font-size:13px;color:#555}
.trip-price .amount{display:block;font-family:Roboto,sans-serif;font-weight:700;font-size:27px;color:var(--navy);letter-spacing:.5px}
.btn-details{position:absolute;right:0;top:62px;width:139px;height:37px;background:var(--blue);color:var(--white);font-weight:700;font-size:14px;display:flex;align-items:center;justify-content:center;gap:5px}

.pager{position:absolute;left:414px;top:2633px;display:flex;gap:8px;align-items:center}
.pager span{width:34px;height:34px;border:1px solid var(--line);background:var(--white);display:flex;align-items:center;justify-content:center;font-weight:500;font-size:18px;color:var(--ink)}
.pager span.current{background:var(--navy);color:var(--white);border-color:var(--navy)}
.pager .dots{width:auto;border:none;background:none;letter-spacing:3px;padding:0 4px}

/* newsletter */
.newsletter{position:absolute;left:0;top:2793px;width:1200px;height:484px;background:linear-gradient(180deg,#f3f3f4 0%,#eeeff1 55%,#e6e9ec 100%);border-top:1px solid #e8e8e8}
.nl-icon{position:absolute;left:553px;top:86px}
.newsletter h2{position:absolute;left:0;top:190px;width:1200px;text-align:center;font-family:Lato,sans-serif;font-weight:900;font-size:38px;color:var(--ink)}
.nl-sub{position:absolute;left:0;top:243px;width:1200px;text-align:center;font-size:14px;color:#555}
.nl-form{position:absolute;left:278px;top:301px;width:643px;height:53px;display:flex}
.nl-input{flex:1;border:1px solid var(--blue);background:var(--white);font-size:14px;color:#444;display:flex;align-items:center;padding-left:24px}
.nl-btn{width:162px;background:var(--blue);color:var(--white);font-weight:500;font-size:20px;display:flex;align-items:center;justify-content:center}
.contacts{position:absolute;left:0;top:392px;width:1200px;display:flex;justify-content:center;align-items:center;gap:26px;font-size:16px;color:#333}
.contacts .item{display:flex;align-items:center;gap:14px}
.contacts .sep{width:1px;height:26px;background:#ccc}

/* footer */
.site-footer{position:absolute;left:0;top:3277px;width:1200px;height:55px;background:var(--footer);color:var(--white);font-size:15px}
.copyright{position:absolute;left:111px;top:18px}
.copyright .div{margin:0 16px}
.socials{position:absolute;left:889px;top:12px;display:flex;gap:12px}
.socials span{width:30px;height:30px;border:2px solid var(--white);border-radius:50%}
</style>
</head>
<body>
<div class="top-rule"></div>

<header class="site-header">
  <div class="brand">VERDALUNEX</div>
  <nav class="main-nav">
    <a>HOME</a><a>ABOUT US</a><a>TRIP</a><a>REVIEWS</a><a>CONTACT</a>
  </nav>
  <div class="btn-signup">
    <svg width="12" height="14" viewBox="0 0 12 14"><circle cx="6" cy="4" r="3.5" fill="#fff"/><path d="M0 14c0-4 2.5-6 6-6s6 2 6 6z" fill="#fff"/></svg>SIGN UP
  </div>
</header>

<section class="hero" role="img" aria-label="Venice canal at dusk with lit palazzos and gondolas">
  <div class="hero-title">TRAVEL EXPERIENCES</div>
  <div class="hero-sub">Lorem ipsum dolor sit amet consectetur adipiscing elit sed do eiusmod tempor sit amet consect incididunt.</div>
  <div class="hero-arrow prev"><svg width="14" height="22" viewBox="0 0 14 22"><path d="M11 2 3 11l8 9" stroke="#fff" stroke-width="3" fill="none"/></svg></div>
  <div class="hero-arrow next"><svg width="14" height="22" viewBox="0 0 14 22"><path d="M3 2l8 9-8 9" stroke="#fff" stroke-width="3" fill="none"/></svg></div>
</section>
<svg class="swoosh left" width="111" height="48" viewBox="0 0 111 48"><path d="M0 8C30 22 70 30 111 30V48C70 46 30 34 0 20z" fill="var(--blue)"/></svg>
<svg class="swoosh right" width="111" height="48" viewBox="0 0 111 48"><path d="M111 8C81 22 41 30 0 30V48C41 46 81 34 111 20z" fill="var(--blue)"/></svg>

<section class="booking">
  <h2>BOOK YOUR TRAVEL TRIPS</h2>
  <div class="field" style="left:53px">
    <label>DESTINATIONS:</label>
    <div class="input">Any Destinations<span class="icon"><svg width="12" height="16" viewBox="0 0 12 16"><path d="M6 0a6 6 0 0 0-6 6c0 4 6 10 6 10s6-6 6-10a6 6 0 0 0-6-6z" fill="#fff"/><circle cx="6" cy="6" r="2.2" fill="var(--blue)"/></svg></span></div>
  </div>
  <div class="field" style="left:352px">
    <label>DATE:</label>
    <div class="input">Select Date &amp; Time<span class="icon"><svg width="14" height="14" viewBox="0 0 14 14"><rect x="0" y="2" width="14" height="12" fill="#fff"/><rect x="0" y="2" width="14" height="3" fill="#dbe9f8"/><path d="M3 7h2M6 7h2M9 7h2M3 10h2M6 10h2M9 10h2" stroke="var(--blue)" stroke-width="1.5"/></svg></span></div>
  </div>
  <div class="field" style="left:651px">
    <label>ACTIVITY:</label>
    <div class="input">Any Category<span class="icon"><svg width="12" height="7" viewBox="0 0 12 7"><path d="M0 0h12L6 7z" fill="#fff"/></svg></span></div>
  </div>
</section>

<!-- sidebar -->
<aside>
  <div class="widget" style="top:925px">
    <div class="widget-tab">DESTINATIONS</div>
    <div class="widget-body" style="height:172px">
      <ul class="link-list"><li>Europe</li><li>Asia &amp; Oceania</li><li>Africa &amp; the Middle East</li><li>The Americas &amp; Caribbean</li></ul>
    </div>
  </div>
  <div class="widget" style="top:1173px">
    <div class="widget-tab">ARRIVAL DATE</div>
    <div class="widget-body" style="height:258px">
      <ul class="opt-list">
        <li><span class="radio"></span>2019 May (888)</li>
        <li><span class="radio"></span>2019 June (7777)</li>
        <li><span class="radio on"></span>2019 July (1111)</li>
        <li><span class="radio"></span>2019 August (555)</li>
        <li><span class="radio"></span>2019 September (5887)</li>
      </ul>
      <div class="btn-date"><svg width="12" height="12" viewBox="0 0 14 14"><rect y="2" width="14" height="12" fill="#fff"/><path d="M3 7h2M6 7h2M9 7h2M3 10h2M6 10h2M9 10h2" stroke="var(--navy)" stroke-width="1.5"/></svg>SELECT A SPECIFIC DATE</div>
    </div>
  </div>
  <div class="widget" style="top:1506px">
    <div class="widget-tab">CATEGORIES</div>
    <div class="widget-body" style="height:391px">
      <ul class="link-list">
        <li>Accommodation type</li><li>Activity</li><li>Audience</li><li>Budget</li><li>Duration</li><li>Experience level</li><li>Experience Types</li><li>Focus/Atmosphere</li><li>Food</li><li>Intensity Level</li><li>Location</li>
      </ul>
    </div>
  </div>
  <div class="widget" style="top:1975px">
    <div class="widget-tab">PRICE PER TRIP</div>
    <div class="widget-body" style="height:172px">
      <ul class="opt-list">
        <li><span class="radio"></span>From US$0 to 112 (298)</li>
        <li><span class="radio"></span>From US$112 to 336 (50)</li>
        <li><span class="radio"></span>From US$336 to 1,007 (70)</li>
        <li><span class="radio"></span>More than US$1,007 (99)</li>
      </ul>
    </div>
  </div>
  <div class="widget" style="top:2224px">
    <div class="widget-tab">DURATION</div>
    <div class="widget-body" style="height:172px">
      <ul class="opt-list">
        <li><span class="check"></span>2 days (787)</li>
        <li><span class="check"></span>From 3 to 7 days (8545)</li>
        <li><span class="check on"></span>From 1 to 2 weeks (7060)</li>
        <li><span class="check"></span>More than 2 weeks (1890)</li>
      </ul>
    </div>
  </div>
</aside>

<!-- main -->
<main>
  <article class="about">
    <h3>VERDALUNEX</h3>
    <p>Lorem ipsum dolor sit amet, consectetur adipiscing elit, sed do eiusmod tempor incididunt ut labore et dolore magna aliqua. Ut enim ad minim veniam, quis nos trud exercitation ullamco laboris nisi ut aliquip ex ea commodo consequat. Duis aute irure dolor in reprehenderit in voluptate velit esse cillum dolore eu fugiat nulla pariatur. Excepteur sint occaecat cupidatat non proident, sunt in culpa qui officia deserunt mollit anim id est laborum.</p>
    <div class="btn-book">BOOK NOW <svg width="14" height="14" viewBox="0 0 14 14"><circle cx="7" cy="7" r="7" fill="#fff"/><path d="M4 7h5M7 4l3 3-3 3" stroke="var(--blue)" stroke-width="2" fill="none"/></svg></div>
  </article>

  <article class="trip" style="top:1330px">
    <div class="trip-photo" role="img" aria-label="Alpine village with church beside a rushing green river" style="background:linear-gradient(180deg,#5b9ad8 0%,#8fbde0 30%,#3f7a3a 55%,#6e8c4a 75%,#3a5a3a 100%)"></div>
    <h4>Lorem ipsum dolor sit amet consectetur adipiscing eiusmod tempor.</h4>
    <ul class="trip-features">
      <li><svg width="11" height="13" viewBox="0 0 11 13"><path d="M.5.5h7l3 3v9H.5z" fill="none" stroke="var(--blue)"/><path d="M2.5 6h6M2.5 8h6M2.5 10h6" stroke="var(--blue)"/></svg>Flexible cancellation policy</li>
      <li><svg width="13" height="13" viewBox="0 0 13 13"><path d="M13 0 0 6l4 2 1 5 2-3 3 2z" fill="var(--blue)"/></svg>Airport transfer included</li>
      <li><svg width="12" height="13" viewBox="0 0 12 13"><path d="M1 0v5h4V0M3 0v13M9 0c-2 1-2 5 0 6v7" stroke="var(--blue)" stroke-width="1.8" fill="none"/></svg>All meals included</li>
    </ul>
    <div class="trip-price"><span class="from">From</span><span class="amount">US$4,698</span><div class="btn-details">SEE DETAILS <svg width="12" height="12" viewBox="0 0 14 14"><circle cx="7" cy="7" r="7" fill="#fff"/><path d="M4 7h5M7 4l3 3-3 3" stroke="var(--blue)" stroke-width="2" fill="none"/></svg></div></div>
  </article>

  <article class="trip" style="top:1591px">
    <div class="trip-photo" role="img" aria-label="White village with blue domes over the sea at sunset" style="background:linear-gradient(180deg,#6c8fb8 0%,#e9b45a 35%,#4d6d95 55%,#cfd6e4 80%,#8aa3c8 100%)"></div>
    <h4>Lorem ipsum dolor sit amet consectetur adipiscing eiusmod tempor.</h4>
    <ul class="trip-features">
      <li><svg width="11" height="13" viewBox="0 0 11 13"><path d="M.5.5h7l3 3v9H.5z" fill="none" stroke="var(--blue)"/><path d="M2.5 6h6M2.5 8h6M2.5 10h6" stroke="var(--blue)"/></svg>Flexible cancellation policy</li>
      <li><svg width="13" height="13" viewBox="0 0 13 13"><path d="M13 0 0 6l4 2 1 5 2-3 3 2z" fill="var(--blue)"/></svg>Airport transfer included</li>
      <li><svg width="12" height="13" viewBox="0 0 12 13"><path d="M1 0v5h4V0M3 0v13M9 0c-2 1-2 5 0 6v7" stroke="var(--blue)" stroke-width="1.8" fill="none"/></svg>All meals included</li>
    </ul>
    <div class="trip-price"><span class="from">From</span><span class="amount">US$4,698</span><div class="btn-details">SEE DETAILS <svg width="12" height="12" viewBox="0 0 14 14"><circle cx="7" cy="7" r="7" fill="#fff"/><path d="M4 7h5M7 4l3 3-3 3" stroke="var(--blue)" stroke-width="2" fill="none"/></svg></div></div>
  </article>

  <article class="trip" style="top:1852px">
    <div class="trip-photo" role="img" aria-label="Traveller sitting on a sea cliff at golden hour" style="background:linear-gradient(180deg,#e8b27a 0%,#c99a7a 30%,#5a88a8 55%,#2f5c7c 80%,#6a5a48 100%)"></div>
    <h4>Lorem ipsum dolor sit amet consectetur adipiscing eiusmod tempor.</h4>
    <ul class="trip-features">
      <li><svg width="11" height="13" viewBox="0 0 11 13"><path d="M.5.5h7l3 3v9H.5z" fill="none" stroke="var(--blue)"/><path d="M2.5 6h6M2.5 8h6M2.5 10h6" stroke="var(--blue)"/></svg>Flexible cancellation policy</li>
      <li><svg width="13" height="13" viewBox="0 0 13 13"><path d="M13 0 0 6l4 2 1 5 2-3 3 2z" fill="var(--blue)"/></svg>Airport transfer included</li>
      <li><svg width="12" height="13" viewBox="0 0 12 13"><path d="M1 0v5h4V0M3 0v13M9 0c-2 1-2 5 0 6v7" stroke="var(--blue)" stroke-width="1.8" fill="none"/></svg>All meals included</li>
    </ul>
    <div class="trip-price"><span class="from">From</span><span class="amount">US$4,698</span><div class="btn-details">SEE DETAILS <svg width="12" height="12" viewBox="0 0 14 14"><circle cx="7" cy="7" r="7" fill="#fff"/><path d="M4 7h5M7 4l3 3-3 3" stroke="var(--blue)" stroke-width="2" fill="none"/></svg></div></div>
  </article>

  <article class="trip" style="top:2113px">
    <div class="trip-photo" role="img" aria-label="Tall waterfall in a green mountain gorge" style="background:linear-gradient(90deg,#2f4a2c 0%,#5b7a4a 30%,#d9e4ea 48%,#6b8a5a 62%,#2c3f2a 100%)"></div>
    <h4>Lorem ipsum dolor sit amet consectetur adipiscing eiusmod tempor.</h4>
    <ul class="trip-features">
      <li><svg width="11" height="13" viewBox="0 0 11 13"><path d="M.5.5h7l3 3v9H.5z" fill="none" stroke="var(--blue)"/><path d="M2.5 6h6M2.5 8h6M2.5 10h6" stroke="var(--blue)"/></svg>Flexible cancellation policy</li>
      <li><svg width="13" height="13" viewBox="0 0 13 13"><path d="M13 0 0 6l4 2 1 5 2-3 3 2z" fill="var(--blue)"/></svg>Airport transfer included</li>
      <li><svg width="12" height="13" viewBox="0 0 12 13"><path d="M1 0v5h4V0M3 0v13M9 0c-2 1-2 5 0 6v7" stroke="var(--blue)" stroke-width="1.8" fill="none"/></svg>All meals included</li>
    </ul>
    <div class="trip-price"><span class="from">From</span><span class="amount">US$4,698</span><div class="btn-details">SEE DETAILS <svg width="12" height="12" viewBox="0 0 14 14"><circle cx="7" cy="7" r="7" fill="#fff"/><path d="M4 7h5M7 4l3 3-3 3" stroke="var(--blue)" stroke-width="2" fill="none"/></svg></div></div>
  </article>

  <article class="trip" style="top:2374px">
    <div class="trip-photo" role="img" aria-label="Old town towers reflected in a river at sunset" style="background:linear-gradient(180deg,#4f6f95 0%,#b89a7a 30%,#e6a84a 50%,#6a5232 70%,#3a3a3a 100%)"></div>
    <h4>Lorem ipsum dolor sit amet consectetur adipiscing eiusmod tempor.</h4>
    <ul class="trip-features">
      <li><svg width="11" height="13" viewBox="0 0 11 13"><path d="M.5.5h7l3 3v9H.5z" fill="none" stroke="var(--blue)"/><path d="M2.5 6h6M2.5 8h6M2.5 10h6" stroke="var(--blue)"/></svg>Flexible cancellation policy</li>
      <li><svg width="13" height="13" viewBox="0 0 13 13"><path d="M13 0 0 6l4 2 1 5 2-3 3 2z" fill="var(--blue)"/></svg>Airport transfer included</li>
      <li><svg width="12" height="13" viewBox="0 0 12 13"><path d="M1 0v5h4V0M3 0v13M9 0c-2 1-2 5 0 6v7" stroke="var(--blue)" stroke-width="1.8" fill="none"/></svg>All meals included</li>
    </ul>
    <div class="trip-price"><span class="from">From</span><span class="amount">US$4,698</span><div class="btn-details">SEE DETAILS <svg width="12" height="12" viewBox="0 0 14 14"><circle cx="7" cy="7" r="7" fill="#fff"/><path d="M4 7h5M7 4l3 3-3 3" stroke="var(--blue)" stroke-width="2" fill="none"/></svg></div></div>
  </article>

  <nav class="pager">
    <span class="current">1</span><span>2</span><span>3</span><span>4</span><span>5</span>
    <span class="dots">•••••••</span>
    <span><svg width="16" height="16" viewBox="0 0 14 14"><circle cx="7" cy="7" r="7" fill="var(--blue)"/><path d="M4 7h5M7 4l3 3-3 3" stroke="#fff" stroke-width="2" fill="none"/></svg></span>
  </nav>
</main>

<section class="newsletter">
  <svg class="nl-icon" width="72" height="76" viewBox="0 0 72 76" fill="none" stroke="var(--blue)" stroke-width="3">
    <path d="M36 2v8M22 6l4 7M50 6l-4 7M12 14l6 5M60 14l-6 5"/>
    <path d="M4 38 36 16l32 22v34H4z"/>
    <rect x="16" y="28" width="40" height="30" fill="#f1f2f3"/>
    <path d="M24 38h24M24 45h24M24 52h14"/>
    <path d="M4 38l32 22 32-22M4 72l24-20M68 72 44 52"/>
  </svg>
  <h2>Sign Up Our Newsletter</h2>
  <p class="nl-sub">Sign Up for Newslettter on Newly Arrived Post, Advice, Events, Posts &amp; Special Offers...</p>
  <div class="nl-form"><div class="nl-input">Enter Your Email</div><div class="nl-btn">SIGN UP!</div></div>
  <div class="contacts">
    <div class="item"><svg width="22" height="22" viewBox="0 0 22 22"><path d="M5 2 2 5c0 8 7 15 15 15l3-3-4-4-3 2c-3-1-5-4-6-6l2-3z" fill="none" stroke="#555" stroke-width="1.4"/></svg>(+1) 123 456 7890</div>
    <span class="sep"></span>
    <div class="item"><svg width="28" height="20" viewBox="0 0 28 20"><rect x="1" y="1" width="26" height="18" fill="none" stroke="#555" stroke-width="1.4"/><path d="M1 1l13 10L27 1M1 19l10-9M27 19l-10-9" fill="none" stroke="#555" stroke-width="1.4"/></svg>info@verdalunex.com</div>
  </div>
</section>

<footer class="site-footer">
  <div class="copyright">© Copyright 2019 Verdalunex. All Rights Reserved<span class="div">|</span>Privacy Policy</div>
  <div class="socials"><span></span><span></span><span></span><span></span><span></span></div>
</footer>
</body>
</html>
```